Website design for a Recruitment Agency in the Pacific Islands

Website for jobseekers to search for work, employers to list vacancies and also for workers to upload their resumes for possible job prospects.

The website will be called ' Korvani Staffing' and this needs to reflect the Pacific Islanders searching for jobs or working in the fields.
Must be connected to a database that collects details for workers which can be downloaded onto an excel spreadsheet for quick reviews offline
The website must also have an app for ios and android so this can be easily downloaded for individuals who want to do quick job searches without going onto the website.

The main objective of this website is to list job opportunities in all Pacific Island Countries or even overseas which Pacific Islanders can apply.

The theme of fishing means ' there is alot of fish in the sea ' = lots of workers in the Pacific Ocean.

Target Market(s)

Agriculture, Fisheries, constructions and mining

Industry/Entity Type

Agriculture, Constructions and Fisheries

Font styles to use
Other font styles liked:
• Muli

Colors
E54698
E96AAD
F1A4CE
F9D9EA
FCEFF6

Requirements
Must have
• Must have an App, adroid and ios
Nice to have
• - pictures of Pacific Islanders , pictures of Pacific Islanders at work in mines, in fisheries and in agricultures

```html
<!DOCTYPE html>
<html lang="en">
<head>
<meta charset="utf-8">
<title>Korvani Staffing — Find the perfect job for you</title>
<link href="https://fonts.googleapis.com/css2?family=Mulish:wght@400;500;600;700;800&display=swap" rel="stylesheet">
<style>
:root{
  --pink:#E5097F;
  --pink-mid:#E96AAD;
  --pink-soft:#F1A4CE;
  --pink-pale:#F9D9EA;
  --pink-wash:#FCEFF6;
  --ink:#111111;
  --grey:#6b6b6b;
  --line:#cfcfcf;
  --white:#ffffff;
  --black:#000000;
}
*{box-sizing:border-box;margin:0;padding:0}
html,body{width:1200px;height:3902px;overflow:hidden}
body{position:relative;font-family:'Mulish',sans-serif;color:var(--ink);background:var(--white)}
.abs{position:absolute}
a{color:inherit;text-decoration:none}

/* header */
.brand{position:absolute;left:86px;top:30px;font-size:30px;font-weight:500;line-height:1;letter-spacing:-.5px;color:var(--ink)}
.brand-footer{color:var(--white);left:86px;top:3520px}
.nav{position:absolute;top:45px;left:311px;display:flex;gap:29px;font-size:13px}
.nav .active{color:var(--pink)}
.upload{position:absolute;left:1009px;top:32px;width:105px;height:42px;border:1.5px solid #333;border-radius:21px;font-size:13px;display:flex;align-items:center;justify-content:center;gap:8px}

/* hero */
.hero{position:absolute;left:86px;top:108px;width:1028px;height:587px;background:var(--pink);border-radius:45px;overflow:hidden;color:var(--white)}
.hero h1{position:absolute;left:56px;top:55px;font-size:60px;font-weight:600;line-height:68px;letter-spacing:.3px}
.hero .lead{position:absolute;left:56px;top:212px;font-size:16px}
.search{position:absolute;left:56px;top:263px;width:459px;height:79px;background:var(--white);border-radius:40px;color:var(--ink)}
.search .field{position:absolute;top:20px;font-size:13px;color:var(--grey)}
.search .field b{display:block;font-size:15px;color:var(--ink);font-weight:700;margin-top:3px}
.search .divider{position:absolute;left:148px;top:20px;width:1px;height:40px;background:#bbb}
.search .go{position:absolute;right:16px;top:14px;width:115px;height:51px;border-radius:26px;background:var(--pink);color:var(--white);font-size:16px;display:flex;align-items:center;justify-content:center}
.hero h3{position:absolute;left:54px;top:380px;font-size:20px;font-weight:600}
.chip{position:absolute;height:38px;border-radius:19px;background:var(--pink-soft);color:var(--pink);font-size:16px;display:flex;align-items:center;justify-content:center}
.hero-art{position:absolute;left:565px;top:36px;width:394px;height:523px;border-radius:50% 40% 45% 50%;background:radial-gradient(circle at 55% 50%,rgba(255,255,255,.22),rgba(255,255,255,0) 68%)}

/* headings */
.section-title{position:absolute;left:85px;font-size:40px;font-weight:600;letter-spacing:.2px}
.section-sub{position:absolute;left:85px;font-size:13px;color:var(--grey)}

/* job cards */
.job{position:absolute;width:326px;height:316px;border:1.5px solid var(--line);border-radius:38px;background:var(--white)}
.job .cat{position:absolute;left:39px;top:52px;display:flex;align-items:center;gap:13px;font-size:13px}
.cat-icon{width:33px;height:33px;border-radius:8px;background:var(--pink-soft)}
.job h4{position:absolute;left:39px;top:100px;font-size:19px;font-weight:600}
.job .meta{position:absolute;left:39px;top:145px;display:flex;align-items:center;font-size:13px}
.job .meta b{margin:0 21px 0 12px;font-weight:700}
.job .posted{position:absolute;left:39px;top:225px;font-size:12px;color:var(--grey);line-height:19px}
.job .posted b{display:block;color:var(--ink);font-size:13px;font-weight:700}
.job .mark{position:absolute;left:224px;top:211px;width:62px;height:62px;border-radius:14px;background:var(--black)}
.btn-pink{position:absolute;background:var(--pink);color:var(--white);border-radius:27px;display:flex;align-items:center;justify-content:center;gap:8px}

/* about */
.about{position:absolute;left:0;top:1716px;width:1200px;height:520px;background:var(--pink-wash);overflow:hidden}
.about .photo{position:absolute;left:0;top:0;width:1200px;height:520px}
.about p{position:absolute;left:85px;width:540px;font-size:13px;line-height:21px;color:#777}
.btn-outline{position:absolute;border:1.5px solid #333;border-radius:22px;font-size:14px;display:flex;align-items:center;justify-content:center}

/* categories */
.category{position:absolute;top:2426px;width:236px;height:286px;border-radius:40px;background:var(--pink-wash);text-align:center}
.category .icon{position:absolute;left:78px;top:44px;width:80px;height:80px;border-radius:14px;background:var(--white);display:flex;align-items:center;justify-content:center}
.category .icon span{width:40px;height:40px;border-radius:8px;background:var(--pink-pale)}
.category h4{position:absolute;left:0;right:0;top:162px;font-size:20px;font-weight:600}
.category p{position:absolute;left:0;right:0;top:236px;font-size:14px}
.category.active{background:var(--pink);color:var(--white)}
.category.active .icon{background:var(--pink-mid)}
.category.active .icon span{background:var(--pink-soft)}
.dots{position:absolute;top:2756px;left:559px;display:flex;gap:10px;align-items:center}
.dots i{display:block;width:9px;height:7px;border-radius:4px;background:var(--pink-soft)}
.dots i.on{width:42px;background:var(--pink)}

/* contact */
.contact-item{position:absolute;left:86px;display:flex;align-items:center;gap:17px;color:var(--pink);font-weight:700;font-size:16px;line-height:19px}
.contact-item .ic{flex:none;width:43px;height:43px;border-radius:50%;background:var(--white);box-shadow:0 3px 12px rgba(0,0,0,.08);display:flex;align-items:center;justify-content:center}
.form{position:absolute;left:509px;top:2851px;width:605px;height:509px;background:var(--white);box-shadow:0 4px 30px rgba(0,0,0,.08)}
.form h2{position:absolute;left:56px;top:45px;font-size:40px;font-weight:600}
.field-f{position:absolute;width:236px}
.field-f label{display:block;font-size:14px;font-weight:700}
.field-f .ph{display:block;margin-top:12px;font-size:12px;color:#aaa;height:16px}
.field-f .rule{margin-top:9px;height:1px;background:#999}

/* footer */
.footer{position:absolute;left:0;top:3447px;width:1200px;height:455px;background:var(--black);color:var(--white)}
.footer .about-text{position:absolute;left:86px;top:159px;width:345px;font-size:14px;line-height:21px}
.footer h5{position:absolute;top:73px;font-size:17px;font-weight:700}
.footer h5::after{content:"";position:absolute;left:0;top:34px;width:42px;height:3px;background:var(--pink)}
.footer ul{position:absolute;top:140px;list-style:none;font-size:12px}
.footer ul li{height:42px}
.footer ul li::before{content:"»";margin-right:13px;color:#bbb}
.footer .fc{position:absolute;left:864px;display:flex;gap:14px;font-size:11px;line-height:14px;width:250px}
.footer .fc b{font-weight:700}
.footer .copy{position:absolute;left:86px;top:366px;width:1028px;display:flex;align-items:center;gap:14px;font-size:13px}
.footer .copy::before,.footer .copy::after{content:"";flex:1;height:1px;background:#666}
</style>
</head>
<body>

<header>
  <div class="brand">Korvani Staffing</div>
  <nav class="nav">
    <a class="active">Home</a><a>About Us</a><a>Services We Offer Assistance In</a><a>Job Seeker Portal</a><a>Training</a><a>Info</a><a>Contact Us</a>
  </nav>
  <a class="upload">Upload
    <svg width="14" height="14" viewBox="0 0 14 14" fill="none" stroke="#111" stroke-width="1.4"><path d="M7 10V2M4 5l3-3 3 3M2 9v3h10V9"/></svg>
  </a>
</header>

<section class="hero">
  <div class="hero-art" role="img" aria-label="Line-drawn shrimp constellation decoration"></div>
  <h1>Find the perfect<br>job for you</h1>
  <p class="lead">Search your career opportunity through 12,800 jobs</p>
  <div class="search">
    <div class="field" style="left:37px">What<b>Job Title</b></div>
    <div class="divider"></div>
    <div class="field" style="left:170px">Where &#8964;<b>All Locations</b></div>
    <a class="go">Find Jobs</a>
  </div>
  <h3>Popular Searches</h3>
  <span class="chip" style="left:56px;top:428px;width:135px">Agriculture</span>
  <span class="chip" style="left:200px;top:428px;width:119px">Fisheries</span>
  <span class="chip" style="left:56px;top:480px;width:214px">Constructions &amp; mining</span>
</section>

<h2 class="section-title" style="top:770px">Featured Job-seeker Portal</h2>
<p class="section-sub" style="top:834px">Search your career opportunity through 12,800 jobs</p>

<svg width="0" height="0" style="position:absolute">
  <symbol id="globe" viewBox="0 0 20 20"><g fill="none" stroke="#333" stroke-width="1.2"><circle cx="10" cy="10" r="8.5"/><path d="M1.5 10h17M10 1.5c3 3 3 14 0 17M10 1.5c-3 3-3 14 0 17"/></g></symbol>
</svg>

<article class="job" style="left:86px;top:889px">
  <div class="cat"><span class="cat-icon"></span>Agriculture</div>
  <h4>Agriculture Dept.</h4>
  <div class="meta"><svg width="22" height="22"><use href="#globe"/></svg><b>Papua New Guinea</b>Full Time</div>
  <div class="posted">June 8, 2022 by<b>Korvani Staffing</b></div>
  <div class="mark"></div>
</article>
<article class="job" style="left:436px;top:889px">
  <div class="cat"><span class="cat-icon"></span>Fisheries</div>
  <h4>Fisheries Dept.</h4>
  <div class="meta"><svg width="22" height="22"><use href="#globe"/></svg><b>Australia</b>Internship</div>
  <div class="posted">June 8, 2022 by<b>Korvani Staffing</b></div>
  <div class="mark"></div>
</article>
<article class="job" style="left:788px;top:889px">
  <div class="cat"><span class="cat-icon"></span>Construction</div>
  <h4>Constructions &amp; mining</h4>
  <div class="meta"><svg width="22" height="22"><use href="#globe"/></svg><b>Papua New Guinea</b>Part Time</div>
  <div class="posted">June 8, 2022 by<b>Korvani Staffing</b></div>
  <div class="mark"></div>
</article>
<article class="job" style="left:86px;top:1239px">
  <div class="cat"><span class="cat-icon"></span>Construction</div>
  <h4>Constructions &amp; mining</h4>
  <div class="meta"><svg width="22" height="22"><use href="#globe"/></svg><b>Papua New Guinea</b>Part Time</div>
  <div class="posted">June 8, 2022 by<b>Korvani Staffing</b></div>
  <div class="mark"></div>
</article>
<article class="job" style="left:436px;top:1239px">
  <div class="cat"><span class="cat-icon"></span>Agriculture</div>
  <h4>Agriculture Dept.</h4>
  <div class="meta"><svg width="22" height="22"><use href="#globe"/></svg><b>Papua New Guinea</b>Full Time</div>
  <div class="posted">June 8, 2022 by<b>Korvani Staffing</b></div>
  <div class="mark"></div>
</article>
<article class="job" style="left:788px;top:1239px">
  <div class="cat"><span class="cat-icon"></span>Fisheries</div>
  <h4>Fisheries Dept.</h4>
  <div class="meta"><svg width="22" height="22"><use href="#globe"/></svg><b>Australia</b>Internship</div>
  <div class="posted">June 8, 2022 by<b>Korvani Staffing</b></div>
  <div class="mark"></div>
</article>

<a class="btn-pink" style="left:86px;top:1577px;width:158px;height:53px;font-size:16px">All Job Offer <span style="font-size:12px">&#8250;</span></a>

<section class="about">
  <svg class="photo" viewBox="0 0 1200 520" role="img" aria-label="Photo of a man working on a laptop while sitting on logs outdoors">
    <defs><linearGradient id="photoTone" x1="0" y1="0" x2="1" y2="1"><stop offset="0" stop-color="#8a8f7a"/><stop offset=".5" stop-color="#a69b88"/><stop offset="1" stop-color="#5f5a52"/></linearGradient></defs>
    <polygon points="856,0 1200,0 1200,520 909,520 667,375" fill="url(#photoTone)"/>
  </svg>
  <h2 class="section-title" style="top:96px">About Korvani Staffing</h2>
  <p style="top:180px">Lorem ipsum dolor sit amet, consectetur adipiscing elit. Praesent ut vehicula lectus. Integer suscipit erat in ligula molestie finibus. Proin ornare ipsum eget risus facilisis volutpat. Nunc tincidunt enim a sapien porttitor, non elementum metus placerat. Curabitur tristique metus at bibendum viverra. Cras hendrerit pellentesque nunc, a cursus leo aliquet sit ame</p>
  <p style="top:296px">Lorem ipsum dolor sit amet, consectetur adipiscing elit. Praesent ut vehicula lectus. Integer suscipit erat in ligula molestie finibus. Proin ornare ipsum eget risus facilisis volutpat.</p>
  <a class="btn-outline" style="left:86px;top:372px;width:122px;height:41px">Get Started</a>
</section>

<h2 class="section-title" style="top:2312px">Search by Category</h2>
<p class="section-sub" style="top:2375px">Search your career opportunity with our categories</p>
<a class="abs" style="left:1012px;top:2318px;font-size:16px;color:var(--pink)">All Category &#8250;</a>

<div class="category" style="left:86px"><div class="icon" role="img" aria-label="Agriculture pictogram"><span></span></div><h4>Agriculture</h4><p>1 open position</p></div>
<div class="category active" style="left:350px"><div class="icon" role="img" aria-label="Fisheries pictogram"><span></span></div><h4>Fisheries</h4><p>1 open position</p></div>
<div class="category" style="left:612px"><div class="icon" role="img" aria-label="Construction pictogram"><span></span></div><h4>Constructions</h4><p>1 open position</p></div>
<div class="category" style="left:876px"><div class="icon" role="img" aria-label="Mining pictogram"><span></span></div><h4>Mining</h4><p>1 open position</p></div>
<div class="dots"><i class="on"></i><i></i><i></i></div>

<h2 class="section-title" style="top:2917px">Contact Us</h2>
<div class="contact-item" style="top:3001px"><span class="ic"><svg width="18" height="18" viewBox="0 0 24 24"><path fill="#E5097F" d="M6.6 10.8a15 15 0 0 0 6.6 6.6l2.2-2.2c.3-.3.7-.4 1-.2 1.1.4 2.3.6 3.6.6.6 0 1 .4 1 1V20c0 .6-.4 1-1 1A17 17 0 0 1 3 4c0-.6.4-1 1-1h3.5c.6 0 1 .4 1 1 0 1.3.2 2.5.6 3.6.1.3 0 .7-.2 1z"/></svg></span>Call: 0412 555 018 (Australia)</div>
<div class="contact-item" style="top:3066px"><span class="ic"><svg width="18" height="18" viewBox="0 0 24 24"><path fill="#E5097F" d="M6.6 10.8a15 15 0 0 0 6.6 6.6l2.2-2.2c.3-.3.7-.4 1-.2 1.1.4 2.3.6 3.6.6.6 0 1 .4 1 1V20c0 .6-.4 1-1 1A17 17 0 0 1 3 4c0-.6.4-1 1-1h3.5c.6 0 1 .4 1 1 0 1.3.2 2.5.6 3.6.1.3 0 .7-.2 1z"/></svg></span>Call: 0412 555 018 (Papua New Guinea)</div>
<div class="contact-item" style="top:3128px"><span class="ic"><svg width="18" height="14" viewBox="0 0 18 14"><rect x="0" y="0" width="18" height="14" rx="2" fill="#E5097F"/><path d="M1 1l8 6 8-6" stroke="#fff" stroke-width="1.5" fill="none"/></svg></span>Email: hello@korvanistaffing.com</div>
<div class="contact-item" style="top:3193px"><span class="ic"><svg width="14" height="18" viewBox="0 0 14 18"><path fill="#E5097F" d="M7 0a7 7 0 0 0-7 7c0 5 7 11 7 11s7-6 7-11a7 7 0 0 0-7-7zm0 9.5A2.5 2.5 0 1 1 7 4.5a2.5 2.5 0 0 1 0 5z"/></svg></span>Location: Papua New Guinea &amp;<br>Australia</div>

<form class="form">
  <h2>Get in Touch</h2>
  <div class="field-f" style="left:56px;top:120px"><label>First Name</label><span class="ph" style="color:#333">|</span><div class="rule"></div></div>
  <div class="field-f" style="left:311px;top:120px"><label>Last Name</label><span class="ph">Jhon Doe</span><div class="rule"></div></div>
  <div class="field-f" style="left:56px;top:206px"><label>Email</label><span class="ph">info@example.com</span><div class="rule"></div></div>
  <div class="field-f" style="left:311px;top:206px"><label>Phone</label><span class="ph">+01 234 567 89</span><div class="rule"></div></div>
  <div class="field-f" style="left:56px;top:290px;width:491px"><label>Your Message</label><span class="ph">Your message here</span><div class="rule" style="margin-top:44px"></div></div>
  <a class="btn-pink" style="left:423px;top:400px;width:124px;height:43px;font-size:16px">Submit</a>
</form>

<footer class="footer">
  <div class="brand" style="color:#fff;top:73px">Korvani Staffing</div>
  <p class="about-text">Praesent eu magna ultricies, aliquet eros a, dignissim ligula. Fusce bibendum sed dui sed ultrices. Phasellus sapien tortor, accumsan quis odio sit amet, aliquet auctor mi. Aliquam vulputate tortor ex, laoreet sodales libero tempus quis. Integer convallis porttitor venenatis.</p>
  <h5 style="left:497px">Quick Links</h5>
  <ul style="left:499px"><li>Home</li><li>About Us</li><li>Services</li><li>Job Seeker portal</li><li>Training</li></ul>
  <h5 style="left:679px">Other Links</h5>
  <ul style="left:681px;top:138px"><li>Our Team</li><li>Gallery</li><li>FAQ</li><li>Reviews</li><li>Contact</li></ul>
  <h5 style="left:864px">Contact</h5>
  <div class="fc" style="top:139px"><svg width="14" height="18" viewBox="0 0 14 18" style="flex:none"><path fill="#fff" d="M7 0a7 7 0 0 0-7 7c0 5 7 11 7 11s7-6 7-11a7 7 0 0 0-7-7zm0 9.5A2.5 2.5 0 1 1 7 4.5a2.5 2.5 0 0 1 0 5z"/></svg><span><b>Location:</b> Papua New Guinea &amp; Australia</span></div>
  <div class="fc" style="top:198px"><svg width="14" height="14" viewBox="0 0 24 24" style="flex:none"><path fill="#fff" d="M6.6 10.8a15 15 0 0 0 6.6 6.6l2.2-2.2c.3-.3.7-.4 1-.2 1.1.4 2.3.6 3.6.6.6 0 1 .4 1 1V20c0 .6-.4 1-1 1A17 17 0 0 1 3 4c0-.6.4-1 1-1h3.5c.6 0 1 .4 1 1 0 1.3.2 2.5.6 3.6.1.3 0 .7-.2 1z"/></svg><span><b>Call:</b> 0412 555 018 (Papua New Guinea)</span></div>
  <div class="fc" style="top:248px"><svg width="14" height="14" viewBox="0 0 24 24" style="flex:none"><path fill="#fff" d="M6.6 10.8a15 15 0 0 0 6.6 6.6l2.2-2.2c.3-.3.7-.4 1-.2 1.1.4 2.3.6 3.6.6.6 0 1 .4 1 1V20c0 .6-.4 1-1 1A17 17 0 0 1 3 4c0-.6.4-1 1-1h3.5c.6 0 1 .4 1 1 0 1.3.2 2.5.6 3.6.1.3 0 .7-.2 1z"/></svg><span><b>Call:</b> 0412 555 018 (Australia)</span></div>
  <div class="fc" style="top:285px"><svg width="14" height="11" viewBox="0 0 18 14" style="flex:none"><rect width="18" height="14" rx="2" fill="#fff"/><path d="M1 1l8 6 8-6" stroke="#000" stroke-width="1.5" fill="none"/></svg><span><b>Email:</b> hello@korvanistaffing.com</span></div>
  <div class="copy">Copyright © 2022. All right reserved.</div>
</footer>

</body>
</html>
```